Business Card Design Project

We need a Business Card for an Mechanical Engineering firm in Singapore. The design should be Modern & Technical looking, yet eye catching.

Our company deals in Cutting Tools & Machine Accessories for the Manufacturing Industries such as Oil & Gas, Aero Space, etc... For more information on our Company, you can either email me or view our website www.valtrion.com.sg.

We are trying to revamp our image to give our consumers a fresh new perspective to our company, so we welcome all ideas.

Industry/Entity Type

Business

Requirements
Must have
• Must incorporate New Company Logo into the card as shown in Uploaded file.

```html
<!DOCTYPE html>
<html lang="en">
<head>
<meta charset="utf-8">
<title>Valtrion Tools – Business Card</title>
<link rel="stylesheet" href="https://fonts.googleapis.com/css2?family=PT+Sans:ital,wght@0,400;0,700;1,400&display=swap">
<style>
  :root {
    --maroon: #8a0f35;
    --paper: #ffffff;
    --edge: #9a9a9a;
  }
  html, body {
    margin: 0;
    padding: 0;
    width: 1200px;
    height: 716px;
    overflow: hidden;
    background: var(--paper);
    font-family: "PT Sans", Arial, sans-serif;
  }
  .canvas {
    position: relative;
    width: 1200px;
    height: 716px;
    background: var(--paper);
  }
  .card {
    position: absolute;
    left: 15px;
    top: 4px;
    width: 1178px;
    height: 634px;
    border: 2px solid var(--edge);
    background: var(--paper);
    overflow: hidden;
  }
  .name-tab {
    position: absolute;
    right: 0;
    top: 0;
    width: 650px;
    height: 146px;
    background: var(--maroon);
    border-bottom-left-radius: 120px 146px;
  }
  .name-tab__label {
    position: absolute;
    left: 206px;
    top: 60px;
    margin: 0;
    color: var(--paper);
    font-style: italic;
    font-size: 27px;
    line-height: 36px;
    white-space: nowrap;
  }
  .brand {
    position: absolute;
    left: 39px;
    top: 222px;
    display: flex;
    align-items: center;
    gap: 16px;
  }
  .brand__dot {
    width: 36px;
    height: 36px;
    border-radius: 50%;
    background: var(--maroon);
  }
  .brand__name {
    margin: 0;
    color: var(--maroon);
    font-size: 48px;
    font-weight: 400;
    letter-spacing: 1px;
    line-height: 1;
    white-space: nowrap;
  }
  .contact {
    position: absolute;
    left: 39px;
    top: 410px;
    margin: 0;
    color: var(--maroon);
    font-size: 30px;
    font-weight: 700;
    line-height: 60px;
    font-style: normal;
    white-space: nowrap;
  }
  .contact p { margin: 0; }
</style>
</head>
<body>
<div class="canvas">
  <div class="card">
    <div class="name-tab">
      <p class="name-tab__label">Name: XXXXXXXX XXXX XXX</p>
    </div>

    <div class="brand">
      <span class="brand__dot" aria-hidden="true"></span>
      <h1 class="brand__name">VALTRION TOOLS</h1>
    </div>

    <address class="contact">
      <p class="contact__address">27 Kallang Way #05-12 * Kestrel Industrial Hub * Singapore 349201</p>
      <p class="contact__phone">Tel: 65-61230457 * Fax: 65-61230458</p>
      <p class="contact__web">Email: hello@valtrion.com.sg * Web: www.valtrion.com.sg</p>
    </address>
  </div>
</div>
</body>
</html>
```